modern, IT themed business card for IT accelerator

Design a business card for tech oriented business accelerator. Prevailing color shall be orange.
we are operating in emerging markets and our mission is to provide co-working space, mentorship/coaching and ultimately seed financing IT startups.
also, we are helping financed ITs in obtaining next round financing, and to this end we are meeting with non IT/finance people and investment professionals..
that means card shall be designed to "impress" not only IT people (mostly liberal) but finance (more conservative)

Industry/Entity Type

Investment

Contact Information for Business Card

Company Name: Orin Venture Yard
Name: Levan Kutateli
Position: Partner
Address: 14, Marjanishvili Ave., Tbilisi 0112, Georgia
Tel: +995599348817
Email: l.kutateli@orinyard.ge
Website: www.orinyard.ge

Font styles to use
Sans Serif

Requirements
Must have
• Attached are logos of the company (portrait & landscape) choose any
Nice to have
• industry is IT and finance (in fact, financing IT startups). therefore design might have IT theme (inspiration from web or software designs)

```html
<!DOCTYPE html>
<html lang="en">
<head>
<meta charset="utf-8">
<title>Orin Venture Yard – Business Card</title>
<link href="https://fonts.googleapis.com/css2?family=Exo+2:wght@400;500;600&display=swap" rel="stylesheet">
<style>
  :root {
    --stage: #ebe8e3;
    --card: #ffffff;
    --slate: #8c8c8c;
    --slate-text: #7b7b7b;
    --orange: #f7941d;
    --ink-light: #ffffff;
  }
  * { box-sizing: border-box; margin: 0; padding: 0; }
  html, body {
    width: 1200px; height: 899px; overflow: hidden;
    background: var(--stage);
    font-family: "Exo 2", Arial, sans-serif;
  }
  .stage { position: relative; width: 1200px; height: 899px; }
  .card {
    position: absolute; left: 280px;
    width: 640px; height: 366px;
    background: var(--card);
    box-shadow: 0 10px 28px rgba(0,0,0,.18);
    overflow: hidden;
  }
  .card--front { top: 52px; }
  .card--back { top: 470px; }
  .card__shapes { position: absolute; inset: 0; width: 640px; height: 366px; }
  .shape-slate { fill: var(--slate); }
  .shape-accent { fill: var(--orange); }

  .front__web {
    position: absolute; left: 30px; top: 190px;
    color: var(--ink-light); font-size: 15px; letter-spacing: .5px;
  }
  .brand {
    position: absolute; display: flex; align-items: center;
    color: var(--slate-text); font-weight: 600;
    text-transform: uppercase; line-height: 1.1;
  }
  .brand__dot { border-radius: 50%; background: var(--orange); flex: none; }
  .brand--front { left: 338px; top: 146px; gap: 16px; font-size: 30px; }
  .brand--front .brand__dot { width: 60px; height: 60px; }
  .brand--back {
    left: 30px; top: 62px; width: 220px;
    flex-direction: column; gap: 22px; text-align: center;
    font-size: 30px;
  }
  .brand--back .brand__dot { width: 110px; height: 110px; }

  .contact {
    position: absolute; right: 34px; top: 34px;
    color: var(--ink-light); text-align: right;
  }
  .contact__name { font-size: 19px; font-weight: 500; letter-spacing: 2px; text-transform: uppercase; }
  .contact__role { font-size: 14px; margin-top: 2px; }
  .contact__address { font-size: 14px; line-height: 1.45; margin-top: 34px; }
  .contact__list { list-style: none; margin-top: 26px; font-size: 13px; }
  .contact__list li {
    display: flex; justify-content: flex-end; align-items: center;
    gap: 8px; height: 22px;
  }
  .contact__icon { width: 14px; height: 14px; fill: none; stroke: var(--ink-light); stroke-width: 1.4; }
</style>
</head>
<body>
<main class="stage">

  <section class="card card--front" aria-label="Card front">
    <svg class="card__shapes" viewBox="0 0 640 366" aria-hidden="true">
      <polygon class="shape-slate" points="0,0 150,0 262,165 205,366 0,366"/>
      <polygon class="shape-accent" points="150,0 180,0 300,168 222,366 205,366 262,165"/>
    </svg>
    <p class="front__web">www.orinyard.ge</p>
    <div class="brand brand--front">
      <span class="brand__dot"></span>
      <span class="brand__name">Orin Venture<br>Yard</span>
    </div>
  </section>

  <section class="card card--back" aria-label="Card back">
    <svg class="card__shapes" viewBox="0 0 640 366" aria-hidden="true">
      <polygon class="shape-slate" points="244,0 640,0 640,366 300,366 348,165"/>
      <polygon class="shape-accent" points="212,0 244,0 348,165 300,366 272,366 318,170"/>
    </svg>

    <div class="brand brand--back">
      <span class="brand__dot"></span>
      <span class="brand__name">Orin Venture<br>Yard</span>
    </div>

    <div class="contact">
      <p class="contact__name">Levan Kutateli</p>
      <p class="contact__role">Partner</p>
      <p class="contact__address">14, Marjanishvili Ave.,<br>Tbilisi 0112</p>
      <ul class="contact__list">
        <li>+995599348817
          <svg class="contact__icon" viewBox="0 0 14 14"><path d="M3 1.5l2 2.5-1.2 1.5c.8 1.8 2 3 3.8 3.8L9 8l2.5 2-1 2.5C6 12 2 8 1.5 3.5z"/></svg>
        </li>
        <li>+995599348817
          <svg class="contact__icon" viewBox="0 0 14 14"><rect x="3.5" y="1" width="7" height="12" rx="1.2"/><line x1="6" y1="11" x2="8" y2="11"/></svg>
        </li>
        <li>+995599348817
          <svg class="contact__icon" viewBox="0 0 14 14"><rect x="1.5" y="5" width="11" height="7" rx="1"/><rect x="4" y="1.5" width="6" height="3.5"/><line x1="4" y1="8.5" x2="10" y2="8.5"/></svg>
        </li>
        <li>l.kutateli@orinyard.ge
          <svg class="contact__icon" viewBox="0 0 14 14"><rect x="1" y="3" width="12" height="8.5"/><polyline points="1,3 7,8 13,3"/></svg>
        </li>
        <li>www.orinyard.ge
          <svg class="contact__icon" viewBox="0 0 14 14"><circle cx="7" cy="7" r="5.8"/><ellipse cx="7" cy="7" rx="2.5" ry="5.8"/><line x1="1.2" y1="7" x2="12.8" y2="7"/></svg>
        </li>
      </ul>
    </div>
  </section>

</main>
</body>
</html>
```